Harborlight Capital Estates business card

We are a real estate advisory and investment company. We are specialized in assisting high networth individuals to invest in real estate overseas. We deliver a very personalized service, anticipating all the potential challenges an investor can face, and making it easy and safe for them. We also co-invest with our clients, assuring them that each project will be looked after as it is our own, and at the same time giving them the extra booth on confidence to invest.

We need a business card design. The business card must have a very premium, high-end look, reflecting principles like "commitment", "trust" and "timeless (but contemporary)". We look for long term relationships with our clients, and we grow with their referrals. We are all about conquering the confidence of the clients by always delivering above the expectations performance.

Target Market(s)

High net worth individuals.

Industry/Entity Type

Real Estate

Contact Information for Business Card

Please consider places on the business card for:

Name
Function (bellow name in smaller size text)

Mobile phone
E-mail
Skype ID
WeChat ID

Adress (3 lines)

Also include the following locations references:
PORTUGAL * DUBAI * HONG KONG

Website: www.hcestates-example.com

Requirements
Must have
• Company Logo

```html
<!DOCTYPE html>
<html lang="en">
<head>
<meta charset="utf-8">
<title>Harborlight Capital Estates – Business Card</title>
<link href="https://fonts.googleapis.com/css2?family=Montserrat:wght@400;500;600&display=swap" rel="stylesheet">
<style>
  :root {
    --page: #e9e7e3;
    --card: #111214;
    --card-edge: #1c1d20;
    --accent: #2fa9e6;
    --text: #d9dadc;
    --muted: #a9abb0;
    --rule: #5a5c61;
  }
  * { box-sizing: border-box; margin: 0; padding: 0; }
  html, body { width: 1200px; height: 900px; overflow: hidden; }
  body {
    background: var(--page);
    font-family: "Montserrat", Arial, sans-serif;
    display: flex;
    flex-direction: column;
    align-items: center;
    justify-content: center;
    gap: 50px;
  }
  .card {
    position: relative;
    width: 600px;
    height: 340px;
    background: var(--card);
    border: 1px solid var(--card-edge);
    border-radius: 22px;
    color: var(--text);
    box-shadow: 0 8px 24px rgba(0,0,0,.18);
  }

  /* Front */
  .card-front .brand {
    position: absolute;
    left: 0; right: 0; top: 112px;
    text-align: center;
  }
  .brand-name {
    display: inline-flex;
    align-items: center;
    gap: 12px;
    font-weight: 500;
    font-size: 30px;
    letter-spacing: 1px;
    color: var(--accent);
  }
  .brand-mark {
    width: 14px; height: 14px;
    border-radius: 50%;
    background: var(--accent);
  }
  .locations {
    position: absolute;
    left: 0; right: 0; top: 196px;
    text-align: center;
    font-size: 14px;
    letter-spacing: 1px;
    color: var(--muted);
  }
  .locations span + span::before { content: "•"; margin: 0 14px; }
  .card-front .website {
    position: absolute;
    left: 0; right: 0; top: 240px;
    text-align: center;
    font-size: 15px;
    color: var(--muted);
  }
  .website .domain { color: var(--accent); }

  /* Back */
  .holder { position: absolute; left: 46px; top: 30px; }
  .holder-name { font-size: 22px; color: var(--accent); font-weight: 400; }
  .holder-role { font-size: 14px; color: var(--muted); margin-top: 2px; }
  .card-back .brand-name {
    position: absolute;
    right: 36px; top: 62px;
    font-size: 19px;
    gap: 9px;
  }
  .card-back .brand-mark { width: 10px; height: 10px; }
  .divider { position: absolute; left: 0; top: 128px; width: 600px; height: 12px; }
  .contacts {
    position: absolute;
    left: 38px; top: 160px;
    list-style: none;
    font-size: 16px;
    color: var(--text);
  }
  .contacts li {
    display: flex; align-items: center; gap: 14px;
    height: 26px;
  }
  .contacts .icon { width: 14px; height: 14px; flex: none; }
  .contacts .dot { width: 13px; height: 13px; border-radius: 50%; background: var(--accent); flex: none; }
  .contacts .dot.alt { background: #4caf3c; }
  .address {
    position: absolute;
    left: 380px; top: 250px;
    font-size: 15px;
    line-height: 20px;
    color: var(--text);
    font-style: normal;
  }
  .address .pin { position: absolute; left: -22px; top: 2px; width: 13px; height: 17px; }
</style>
</head>
<body>

  <section class="card card-front">
    <div class="brand"><span class="brand-name"><span class="brand-mark"></span>Harborlight Capital Estates</span></div>
    <div class="locations"><span>PORTUGAL</span><span>DUBAI</span><span>HONG KONG</span></div>
    <div class="website">www.<span class="domain">hcestates-example</span>.com</div>
  </section>

  <section class="card card-back">
    <div class="holder">
      <h1 class="holder-name">Your Name</h1>
      <p class="holder-role">position</p>
    </div>
    <span class="brand-name"><span class="brand-mark"></span>Harborlight Capital Estates</span>

    <svg class="divider" viewBox="0 0 600 12">
      <path d="M0 6 H96 L102 11 L108 6 H600" fill="none" stroke="var(--rule)" stroke-width="1"/>
    </svg>

    <ul class="contacts">
      <li>
        <svg class="icon" viewBox="0 0 16 16"><path d="M4 1 L6.5 4.5 L5 6.5 C6 8.5 7.5 10 9.5 11 L11.5 9.5 L15 12 L13 15 C7 14 2 9 1 3 Z" fill="var(--muted)"/></svg>
        +1 555 014 2298
      </li>
      <li>
        <svg class="icon" viewBox="0 0 16 16"><rect x="1" y="3" width="14" height="10" fill="none" stroke="var(--muted)" stroke-width="1.5"/><path d="M1 3 L8 9 L15 3" fill="none" stroke="var(--muted)" stroke-width="1.5"/></svg>
        hello@hcestates-example.com
      </li>
      <li><span class="dot"></span>/hcestates</li>
      <li><span class="dot alt"></span>/hcestates</li>
      <li>
        <svg class="icon" viewBox="0 0 16 16"><g fill="none" stroke="var(--muted)" stroke-width="1.2"><circle cx="8" cy="8" r="6.5"/><ellipse cx="8" cy="8" rx="3" ry="6.5"/><path d="M1.5 8 H14.5"/></g></svg>
        <span class="website">www.<span class="domain">hcestates-example</span>.com</span>
      </li>
    </ul>

    <address class="address">
      <svg class="pin" viewBox="0 0 13 17"><path d="M6.5 0 C3 0 0 2.7 0 6.3 C0 10.5 6.5 17 6.5 17 S13 10.5 13 6.3 C13 2.7 10 0 6.5 0 Z" fill="var(--muted)"/><circle cx="6.5" cy="6.3" r="2.3" fill="var(--card)"/></svg>
      Opp. Marlow Street Market<br>
      Linden Jn. Harborside<br>
      Westvale, Coastland
    </address>
  </section>

</body>
</html>
```